Kestrel Photography Business Card

I need a business card designed for a photography business based in Perth, Western Australia called Kestrel Photography.

We specialise in wedding, event photography and portrait photography.

The business card must borrow the style of the attached logo.

The hex codes for the colours in the logo are:
#ED1D85 - Pink
#89C23E - Green
#37282F - Black

The name on the card will be:
Name: Toviran
Phone: 0417395268
Website: www.kestrelphotography.com.au
Facebook: kestrelphotography

I am open and happy to accept creative concepts.

I’d like some space at the back for writing notes and appointment details.

```html
<!DOCTYPE html>
<html lang="en">
<head>
<meta charset="utf-8">
<title>Kestrel Photography – Business Card</title>
<link href="https://fonts.googleapis.com/css2?family=Questrial&display=swap" rel="stylesheet">
<style>
  :root {
    --pink: #ED1D85;
    --green: #A5C545;
    --ink: #37282F;
    --navy: #2C3A4B;
    --paper: #FFFFFF;
    --backdrop: #E6E6E8;
    --type-light: #F2F2F2;
  }
  * { margin: 0; padding: 0; box-sizing: border-box; }
  html, body {
    width: 1200px;
    height: 900px;
    overflow: hidden;
    background: var(--backdrop);
    font-family: "Questrial", "Century Gothic", sans-serif;
  }
  .sheet {
    position: relative;
    width: 1200px;
    height: 900px;
  }
  .card {
    position: absolute;
    box-shadow: 0 6px 18px rgba(0,0,0,0.18);
  }

  /* Front */
  .card-front {
    left: 110px;
    top: 200px;
    width: 525px;
    height: 300px;
    background: var(--paper);
  }
  .brand-mark {
    position: absolute;
    left: 50%;
    top: 78px;
    width: 64px;
    height: 64px;
    margin-left: -32px;
    border-radius: 50%;
    background: var(--pink);
  }
  .brand-name {
    position: absolute;
    left: 0;
    right: 0;
    top: 170px;
    text-align: center;
    font-size: 17px;
    letter-spacing: 9px;
    text-transform: uppercase;
    color: var(--ink);
    padding-left: 9px;
  }

  /* Back */
  .card-back {
    left: 745px;
    top: 100px;
    width: 320px;
    height: 560px;
    background: var(--navy);
    color: var(--type-light);
  }
  .contact {
    position: absolute;
    left: 30px;
    top: 34px;
  }
  .contact-name {
    font-size: 30px;
    color: var(--pink);
    line-height: 1.05;
  }
  .contact-role {
    font-size: 22px;
    line-height: 1.2;
  }
  .contact-phone {
    margin-top: 10px;
    font-size: 15px;
    letter-spacing: 0.3px;
  }
  .target {
    position: absolute;
    left: 72px;
    top: 190px;
    width: 176px;
    height: 176px;
  }
  .links {
    position: absolute;
    left: 30px;
    bottom: 32px;
    font-size: 14.5px;
    line-height: 1.45;
    letter-spacing: 0.2px;
  }
</style>
</head>
<body>
  <main class="sheet">
    <section class="card card-front" aria-label="Business card front">
      <div class="brand-mark"></div>
      <h1 class="brand-name">Kestrel Photography</h1>
    </section>

    <section class="card card-back" aria-label="Business card back">
      <div class="contact">
        <p class="contact-name">Toviran</p>
        <p class="contact-role">photographer</p>
        <p class="contact-phone">Phone: 0417395268</p>
      </div>

      <svg class="target" viewBox="0 0 176 176" aria-hidden="true">
        <circle cx="88" cy="88" r="88" fill="var(--pink)"/>
        <circle cx="88" cy="88" r="55" fill="var(--green)"/>
      </svg>

      <div class="links">
        <p class="links-web">www.kestrelphotography.com.au</p>
        <p class="links-social">Facebook: kestrelphotography</p>
      </div>
    </section>
  </main>
</body>
</html>
```